HARD MONEY ORIGINATOR RECRUITMENT.
Looking for individuals to help us originate loans for real estate investor financing primarily used to fix up properties and resell.
HARD MONEY ORIGINATORS WANTED
No Licensing Required
Work As Independent Contractor
1% Flat Finders Fee on Each Loan
Referral Compensation for Recruiting New Originators
Immediate Payouts
Programs Offered Nationwide
Marketing Assistance and Support Available
Email mbelton@corvalendgroup.com for more information or call (800) 641-2957 Ext. 24 Corva Lend Group Services, Inc. www.corvalendgroup.com NMLS #731864
Industry/Entity Type
Real Estate
Look and feel

```html
<!DOCTYPE html>
<html lang="en">
<head>
<meta charset="utf-8">
<title>Hard Money Originator Recruitment</title>
<link href="https://fonts.googleapis.com/css2?family=Oswald:wght@600;700&family=Nunito+Sans:wght@400;600;700&display=swap" rel="stylesheet">
<style>
  :root {
    --green: #8cc63f;
    --green-soft: #9fd05a;
    --blue: #1e5f8c;
    --navy: #1f4f7a;
    --ink: #333333;
    --rule: #9a9a9a;
    --white: #ffffff;
  }
  * { margin: 0; padding: 0; box-sizing: border-box; }
  html, body { width: 844px; height: 1200px; overflow: hidden; background: var(--white); }
  .flyer {
    position: relative; width: 844px; height: 1200px; overflow: hidden;
    background: linear-gradient(180deg, #ffffff 0%, #ffffff 86%, #ebebeb 100%);
    font-family: "Nunito Sans", Arial, sans-serif; color: var(--ink);
  }
  .header-accent { position: absolute; left: 0; top: 0; width: 277px; height: 298px; background: var(--green); }
  .header-art {
    position: absolute; left: 40px; top: 40px; width: 200px; height: 200px;
    background: radial-gradient(circle at 50% 50%, var(--green-soft) 0%, var(--green) 75%);
  }
  .header-title {
    position: absolute; left: 277px; top: 0; width: 567px; height: 298px; background: var(--blue);
    padding: 30px 0 0 86px;
    font-family: "Oswald", Impact, sans-serif; font-weight: 700; color: var(--white);
    font-size: 68px; line-height: 75px; letter-spacing: 0.5px;
  }
  .header-pointer { position: absolute; left: 436px; top: 296px; width: 42px; height: 22px; }
  .intro {
    position: absolute; left: 40px; top: 333px; width: 764px; text-align: center;
    font-size: 24px; line-height: 29px; color: var(--ink);
  }
  .rule { position: absolute; left: 42px; width: 760px; height: 2px; background: var(--rule); }
  .rule.top { top: 452px; }
  .rule.bottom { top: 526px; }
  .section-title {
    position: absolute; left: 0; top: 458px; width: 844px; text-align: center;
    font-family: "Oswald", Impact, sans-serif; font-weight: 700; color: var(--navy);
    font-size: 46px; line-height: 62px; letter-spacing: 0.5px;
  }
  .benefits { position: absolute; left: 38px; top: 562px; width: 270px; list-style: none; }
  .benefits li {
    position: relative; padding-left: 18px; margin-bottom: 10px;
    font-size: 18px; line-height: 22px; color: var(--ink);
  }
  .benefits li::before {
    content: ""; position: absolute; left: 0; top: 8px; width: 6px; height: 6px;
    border-radius: 50%; background: var(--ink);
  }
  .photo { position: absolute; width: 218px; height: 147px; }
  .photo.p1 { left: 360px; top: 561px; background: linear-gradient(135deg, #d9d4cc, #8a7a62); }
  .photo.p2 { left: 591px; top: 561px; background: linear-gradient(135deg, #cfd8c2, #7a5a40); }
  .photo.p3 { left: 360px; top: 717px; background: linear-gradient(135deg, #6b8fb3, #3f5d7a); }
  .photo.p4 { left: 591px; top: 717px; background: linear-gradient(135deg, #e8e4dc, #8a8478); }
  .contact-band {
    position: absolute; left: 37px; top: 896px; width: 770px; height: 76px; background: var(--blue);
    color: var(--white); text-align: center; font-size: 23px; line-height: 30px; padding-top: 8px;
  }
  .contact-band strong { font-weight: 700; }
  .brand-mark { position: absolute; left: 46px; top: 1040px; display: flex; align-items: center; gap: 14px; }
  .brand-mark .dot { width: 58px; height: 58px; border-radius: 50%; background: var(--green); }
  .brand-mark .name { font-size: 26px; font-weight: 700; color: var(--navy); }
  .company { position: absolute; left: 340px; top: 1044px; width: 440px; text-align: right; color: var(--navy); }
  .company .name { font-size: 25px; font-weight: 600; line-height: 32px; }
  .company .meta { font-size: 18px; line-height: 24px; color: var(--ink); font-weight: 600; }
</style>
</head>
<body>
<main class="flyer">
  <div class="header-accent">
    <div class="header-art" role="img" aria-label="Icon of a businessperson with a dollar speech bubble"></div>
  </div>
  <h1 class="header-title">HARD MONEY<br>ORIGINATOR<br>RECRUITMENT</h1>
  <svg class="header-pointer" viewBox="0 0 42 22" aria-hidden="true"><path d="M0 0 H42 L21 22 Z" fill="#1e5f8c"/></svg>

  <p class="intro">Looking for individuals to help us originate loans for real<br>estate investor financing primarily used to fix up properties<br>and resell.</p>

  <div class="rule top"></div>
  <h2 class="section-title">HARD MONEY ORIGINATORS WANTED</h2>
  <div class="rule bottom"></div>

  <ul class="benefits">
    <li>No Licensing Required</li>
    <li>Work As Independent<br>Contractor</li>
    <li>1% Flat Finders Fee on<br>Each Loan</li>
    <li>Referral Compensation for<br>Recruiting New Originators</li>
    <li>Immediate Payouts</li>
    <li>Programs Offered Nationwide</li>
    <li>Marketing Assistance and<br>Support Available</li>
  </ul>

  <div class="photo p1" role="img" aria-label="Photo of a man measuring a wall with a tape measure"></div>
  <div class="photo p2" role="img" aria-label="Photo of a worker in a hard hat carrying lumber"></div>
  <div class="photo p3" role="img" aria-label="Photo of a worker in a hard hat renovating an interior"></div>
  <div class="photo p4" role="img" aria-label="Photo of a businesswoman and a contractor reviewing plans in a home"></div>

  <div class="contact-band">
    Email <strong>mbelton@corvalendgroup.com</strong> for more information<br>
    or call <strong>(800) 641-2957</strong> Ext. 24
  </div>

  <div class="brand-mark">
    <span class="dot"></span>
    <span class="name">Corva Lend</span>
  </div>
  <div class="company">
    <p class="name">Corva Lend Group Services, Inc.</p>
    <p class="meta">www.corvalendgroup.com &nbsp;|&nbsp; NMLS #731864</p>
  </div>
</main>
</body>
</html>
```